Mobile Oil Change company needs a flyer to promote new business

We need a flyer to 1) print & handout and 2) email out to potential customers. We are a mobile oil change company that comes to our customer locations to perform the work instead of customers going to traditional oil change companies. We have a 21 point inspection with our oil change. (21 point inspection details will not be on the flyer). Would like to keep the flyer simple but creative. I'm attaching 1) the write-up we created, 2) our logo (logo color is dark teal on white but other combinations are included if you wanted to propose a different color combination), and 3) additional services we offer. Logo font is Alegreya Sans.
Would like the additional services listed with icons and brief descriptions (similar to attachment) without pricing. Company website for reference is www.brindlefleetcare.com.

Target Market(s)

Companies with many service vehicles such as Oil & Gas service companies, heating and air conditioning companies, utility companies, police departments, etc. Companies that prioritize convenience and maintenance first.

Font styles to use
Sans Serif

Colors
00a990

Requirements
Must have
• Simple but creative design with our logo at top of the flyer. Additional Services (details in document supplied) can be smaller and less prominent than other "main" content listed in the CONTENT document supplied.
Should not have
• Do not use animated character graphics in the flyer and limit (1) stock photos to A small area in the flyer.

```html
<!DOCTYPE html>
<html lang="en">
<head>
<meta charset="utf-8">
<title>Brindle Fleet Care – Mobile Oil Change Flyer</title>
<link href="https://fonts.googleapis.com/css2?family=Alegreya+Sans:wght@500;700;800&family=Fira+Sans+Condensed:wght@400;500;600;700&family=Montserrat:wght@700&display=swap" rel="stylesheet">
<style>
  :root {
    --teal-dark: #124c4e;
    --teal-accent: #00a990;
    --teal-bright: #19b99a;
    --white: #ffffff;
    --rule: rgba(255,255,255,0.35);
    --photo-dark: #1d120b;
    --photo-brown: #5a2e16;
    --photo-gold: #b68a3a;
    --photo-light: #e0c27a;
  }
  * { box-sizing: border-box; margin: 0; padding: 0; }
  html, body { width: 870px; height: 1200px; overflow: hidden; background: var(--teal-dark); }
  .flyer { position: relative; width: 870px; height: 1200px; display: flex; font-family: "Fira Sans Condensed", sans-serif; color: var(--white); }

  /* Left photo column */
  .photo-column { position: relative; width: 341px; height: 100%; }
  .photo-fill {
    position: absolute; inset: 0;
    background:
      radial-gradient(ellipse at 55% 42%, var(--photo-light) 0%, var(--photo-gold) 22%, transparent 55%),
      linear-gradient(180deg, var(--photo-brown) 0%, #7a4a22 20%, var(--photo-gold) 42%, #6b4a1e 62%, var(--photo-dark) 80%, #140d08 100%);
  }
  .extras { position: absolute; left: 73px; right: 30px; top: 788px; }
  .extras-title { font-weight: 600; font-size: 17px; letter-spacing: 0.3px; text-transform: uppercase; }
  .extras-rule { height: 1px; background: var(--rule); margin: 14px 0 18px; width: 190px; }
  .extras-list { list-style: none; font-weight: 500; font-size: 17px; line-height: 29.5px; }
  .call-out { position: absolute; left: 73px; top: 1036px; font-family: "Montserrat", sans-serif; font-weight: 700; font-size: 30px; line-height: 36px; text-transform: uppercase; }

  /* Right content panel */
  .content-panel { position: relative; flex: 1; height: 100%; background: var(--teal-dark); text-align: center; }
  .brand { position: absolute; top: 82px; left: 0; right: 0; display: flex; justify-content: center; align-items: center; gap: 14px; }
  .brand-dot { width: 22px; height: 22px; border-radius: 50%; background: var(--teal-bright); }
  .brand-name { font-family: "Alegreya Sans", sans-serif; font-weight: 800; font-size: 48px; line-height: 52px; color: var(--teal-bright); text-transform: uppercase; letter-spacing: 1px; text-align: left; }
  .panel-rule { position: absolute; left: 105px; right: 105px; height: 1px; background: var(--rule); }
  .panel-rule.top { top: 245px; }
  .panel-rule.bottom { top: 1003px; }
  .headline { position: absolute; top: 268px; left: 0; right: 0; font-family: "Alegreya Sans", sans-serif; font-weight: 800; font-size: 28px; line-height: 31px; color: var(--teal-bright); text-transform: uppercase; }
  .intro { position: absolute; top: 350px; left: 40px; right: 40px; font-weight: 600; font-size: 21px; line-height: 25px; }

  .step { position: absolute; width: 230px; margin-left: -115px; text-align: center; }
  .step-icon { width: 76px; height: 76px; margin: 0 auto 8px; border: 2px solid var(--white); border-radius: 10px; display: flex; align-items: center; justify-content: center; }
  .step-icon svg { width: 52px; height: 52px; }
  .step-text { font-size: 15px; line-height: 18px; font-weight: 400; }
  .step.one { left: 159px; top: 438px; }
  .step.two { left: 369px; top: 438px; }
  .step.three { left: 159px; top: 566px; }
  .step.four { left: 369px; top: 566px; }
  .step.five { left: 264px; top: 702px; }

  .highlights { position: absolute; top: 868px; left: 20px; right: 20px; font-weight: 500; font-size: 20px; line-height: 27px; color: var(--teal-bright); }
  .contact { position: absolute; top: 1030px; left: 0; right: 0; font-weight: 600; font-size: 23px; line-height: 29px; }
</style>
</head>
<body>
<main class="flyer">
  <aside class="photo-column">
    <div class="photo-fill" role="img" aria-label="Close-up photograph of a golden engine piston glistening with motor oil"></div>
    <section class="extras">
      <h2 class="extras-title">Additional Services</h2>
      <div class="extras-rule"></div>
      <ul class="extras-list">
        <li>Engine Air Filter Replacement</li>
        <li>Cabin Air Filter Replacement</li>
        <li>Wiperblade Replacement</li>
        <li>Power Steering Fluid Flush</li>
        <li>Fuel System Treatment</li>
        <li>Brake Fluid Flush</li>
      </ul>
    </section>
    <p class="call-out">Call to us<br>today</p>
  </aside>

  <section class="content-panel">
    <div class="brand">
      <span class="brand-dot"></span>
      <span class="brand-name">Brindle<br>Fleet Care</span>
    </div>
    <div class="panel-rule top"></div>

    <h1 class="headline">Hassle free oil<br>changes on your terms</h1>
    <p class="intro">Our simple 5-step process lets you schedule an appointment and get service to save time and money:</p>

    <div class="step one">
      <div class="step-icon">
        <svg viewBox="0 0 52 52" fill="none" stroke="#fff" stroke-width="2.5" stroke-linejoin="round">
          <path d="M14 8 l7 9 -4 5 c2 5 6 9 11 11 l5 -4 9 7 -4 6 c-14 0 -28 -14 -28 -28 z"/>
          <path d="M30 10 a12 12 0 0 1 12 12 M30 16 a6 6 0 0 1 6 6" stroke-linecap="round"/>
        </svg>
      </div>
      <p class="step-text">Call or email us<br>to schedule service</p>
    </div>

    <div class="step two">
      <div class="step-icon">
        <svg viewBox="0 0 52 52" fill="#fff">
          <circle cx="26" cy="10" r="5"/>
          <path d="M18 18 h16 l2 16 h-4 l-1 14 h-10 l-1 -14 h-4 z"/>
        </svg>
      </div>
      <p class="step-text">Our highly trained technicians<br>come to you for service</p>
    </div>

    <div class="step three">
      <div class="step-icon">
        <svg viewBox="0 0 52 52" fill="#fff">
          <path d="M6 10 h24 v20 h-24 z M30 16 h8 l6 8 v6 h-14 z"/>
          <circle cx="13" cy="33" r="3.5"/><circle cx="36" cy="33" r="3.5"/>
          <path d="M14 40 h20 l4 5 v3 h-28 v-3 z"/>
        </svg>
      </div>
      <p class="step-text">Service is performed<br>quickly on your vehicle</p>
    </div>

    <div class="step four">
      <div class="step-icon">
        <svg viewBox="0 0 52 52" fill="none" stroke="#fff" stroke-width="2.5">
          <path d="M10 6 h22 v40 h-22 z" fill="#fff"/>
          <path d="M15 14 h12 M15 20 h12 M15 26 h8" stroke="#124c4e"/>
          <circle cx="36" cy="32" r="9"/>
          <path d="M36 27 v10 M33 30 h5 M33 34 h5" stroke-linecap="round"/>
        </svg>
      </div>
      <p class="step-text">Pay agreed-upon pricing<br>and receipt is emailed to you</p>
    </div>

    <div class="step five">
      <div class="step-icon">
        <svg viewBox="0 0 52 52" fill="none" stroke="#fff" stroke-width="2.5" stroke-linecap="round">
          <rect x="12" y="6" width="20" height="40" rx="3"/>
          <path d="M20 41 h4"/>
          <path d="M37 20 a6 6 0 0 1 0 10 M41 16 a12 12 0 0 1 0 18"/>
        </svg>
      </div>
      <p class="step-text">Services performed<br>are tracked electronically<br>and reminders created</p>
    </div>

    <p class="highlights">High quality synthetic oil used is best suited<br>for commercial vehicles<br>Service includes a 21-point inspection<br>Additional services are available</p>

    <div class="panel-rule bottom"></div>

    <address class="contact" style="font-style: normal;">
      (833) 555-0147<br>
      sales@brindlefleetcare.com<br>
      www.brindlefleetcare.com
    </address>
  </section>
</main>
</body>
</html>
```